Business Card Design for Translation Company - Rush

Rush job for a business card designing for a company doing international translations, several Asian and western languages. Already have a logo design (see attached) to use as the basis of the business card design. For the card, we also need the full company name, address, email, and phone number. In addition, my name as I will be the one handing out the cards.

For the logo design, we think the white background would be best. But we will consider using the dark background if you have a great idea for it.

The attached jpeg design has just been approved, but the designer has not yet finalized the file. When we select our final applicant, we will send the finalized file. (Nothing changes except the quality of the data.)

The phone number may change and if so, we will send the new one when we select our applicant.

We must complete the entire process and have a design ready to go to print no later than 01:00 am August 3, New York (East Coast) time.

We look forward to your participation in the project,
Gus

Target Market(s)

Translation clients worldwide.

Industry/Entity Type

Business

Contact Information for Business Card

Company details:

Korvani Languages Worldwide, Ltd.

#527-2368 Halden Crescent, Victoria, BC, Canada V9T3K2

gdresner@korvanilanguages.example

+1-888-604-2731

Font styles to use
Sans Serif

Requirements
Must have
• Company name, address, email and phone number.
• Also my name:
• Gustav R. Dresner
• Director
Nice to have
• Not a demand, but please consider creatively using the horizontal bar.
Should not have
• Cluttered of jumbled appearance.

```html
<!DOCTYPE html>
<html lang="en">
<head>
<meta charset="utf-8">
<title>Korvani Languages – Business Card</title>
<link href="https://fonts.googleapis.com/css2?family=Montserrat:wght@500;600;700&family=Open+Sans:wght@400;600&display=swap" rel="stylesheet">
<style>
  :root {
    --orange: #e87722;
    --orange-light: #f0a467;
    --charcoal: #3d3d3f;
    --grey: #6b6b6d;
    --paper: #ffffff;
    --backdrop: #e9e6e1;
  }
  * { box-sizing: border-box; margin: 0; padding: 0; }
  html, body { width: 1200px; height: 1024px; overflow: hidden; }
  body { background: var(--backdrop); position: relative; font-family: "Open Sans", sans-serif; }

  .card {
    position: absolute; left: 220px; width: 760px; height: 434px;
    background: var(--paper); overflow: hidden;
    box-shadow: 0 6px 18px rgba(0,0,0,.18);
  }
  .card--front { top: 52px; }
  .card--back { top: 538px; }

  .card__art { position: absolute; inset: 0; width: 100%; height: 100%; }

  .wordmark {
    position: absolute; display: flex; align-items: center; gap: 14px;
    font-family: "Montserrat", sans-serif; font-weight: 600;
    color: var(--charcoal); text-transform: uppercase; letter-spacing: .28em; line-height: 1.25;
  }
  .wordmark__dot { width: 18px; height: 18px; border-radius: 50%; background: var(--orange); flex: none; }
  .wordmark__rule { height: 2px; background: var(--orange); }

  .card--front .wordmark { left: 48px; top: 56px; font-size: 17px; }
  .card--front .wordmark__rule { position: absolute; left: 60px; top: 108px; width: 290px; }

  .holder { position: absolute; left: 48px; top: 296px; }
  .holder__name {
    font-family: "Montserrat", sans-serif; font-weight: 700; font-size: 20px;
    letter-spacing: .06em; text-transform: uppercase; color: var(--charcoal);
  }
  .holder__title { font-family: "Montserrat", sans-serif; font-weight: 600; font-size: 14px; color: var(--orange); margin-top: 2px; }
  .holder__rule { width: 230px; height: 2px; background: var(--orange); margin-top: 8px; }

  .contact { position: absolute; left: 330px; top: 150px; font-size: 13px; line-height: 1.6; color: var(--charcoal); }
  .contact__label { color: var(--orange); font-weight: 600; }

  .card--back .wordmark { left: 80px; top: 250px; font-size: 28px; }
  .card--back .wordmark__dot { width: 26px; height: 26px; }
  .card--back .wordmark__rule { position: absolute; left: 120px; top: 340px; width: 470px; }
</style>
</head>
<body>

<section class="card card--front" aria-label="Business card front">
  <svg class="card__art" viewBox="0 0 760 434" aria-hidden="true">
    <path d="M640 0 H760 V434 H690 C740 300 720 120 640 0 Z" fill="var(--orange)"/>
    <path d="M600 0 C700 110 715 290 660 434" fill="none" stroke="var(--charcoal)" stroke-width="6"/>
    <path d="M0 380 C80 372 180 395 250 434 H0 Z" fill="var(--orange-light)"/>
    <path d="M0 360 C100 352 200 370 280 434 H258 C190 392 90 372 0 378 Z" fill="var(--grey)"/>
  </svg>

  <div class="wordmark">
    <span class="wordmark__dot"></span>
    <span>Korvani<br>Languages</span>
  </div>
  <div class="wordmark__rule"></div>

  <div class="contact">
    <p>Korvani Languages Worldwide, Ltd.</p>
    <p>#527-2368 Halden Crescent, Victoria, BC,</p>
    <p>Canada V9T3K2</p>
    <p style="margin-top:14px"><span class="contact__label">Phone:</span> +1-888-604-2731</p>
    <p><span class="contact__label">E-mail:</span> gdresner@korvanilanguages.example</p>
  </div>

  <div class="holder">
    <p class="holder__name">Gustav R. Dresner</p>
    <p class="holder__title">Director</p>
    <div class="holder__rule"></div>
  </div>
</section>

<section class="card card--back" aria-label="Business card back">
  <div class="wordmark">
    <span class="wordmark__dot"></span>
    <span>Korvani<br>Languages</span>
  </div>
  <div class="wordmark__rule"></div>
</section>

</body>
</html>
```